Cobalt Ridge Mini Storage - Ad for half Page

Need half page ad for a publication.
would also like to be able to use in the future
self storage facility - 3 locations, the third opening soon
do not like real busy projects...i have a logo but willing to tweak if needed

```html
<!DOCTYPE html>
<html lang="en">
<head>
<meta charset="utf-8">
<title>Cobalt Ridge Mini Storage – Coming Soon Ad</title>
<link rel="stylesheet" href="https://fonts.googleapis.com/css2?family=Exo+2:wght@400;600;700&family=Fredoka:wght@700&display=swap">
<style>
  :root {
    --brown: #6b3512;
    --brown-text: #6b3714;
    --gold: #a8731f;
    --panel: #e1e3e2;
    --ink: #333333;
    --tan: #d8c4a0;
    --white: #ffffff;
  }
  * { box-sizing: border-box; margin: 0; padding: 0; }
  html, body { width: 1068px; height: 1200px; overflow: hidden; background: var(--white); }
  .ad {
    position: absolute; left: 241px; top: 161px;
    width: 586px; height: 878px;
    background: var(--panel);
    font-family: "Exo 2", sans-serif;
    overflow: hidden;
  }
  .top-rule { position: absolute; left: 0; top: 0; width: 586px; height: 12px; }
  .brand {
    position: absolute; left: 0; top: 50px; width: 100%;
    display: flex; justify-content: center; align-items: center; gap: 14px;
  }
  .brand-mark { width: 54px; height: 54px; background: var(--gold); }
  .brand-name {
    font-weight: 700; font-size: 28px; line-height: 29px; color: var(--brown-text);
  }
  .garage-art {
    position: absolute; left: 191px; top: 172px; width: 178px; height: 130px;
    background: linear-gradient(var(--tan), #e4d6bb);
  }
  .headline {
    position: absolute; left: 0; top: 262px; width: 100%;
    text-align: center; font-family: "Fredoka", sans-serif; font-weight: 700;
    color: var(--brown-text); font-size: 94px; line-height: 88px; letter-spacing: -2px;
    text-transform: uppercase; text-shadow: 4px 4px 0 #b7b7b7;
  }
  .location {
    position: absolute; left: 224px; top: 486px; width: 138px; height: 41px;
    border-top: 2px solid var(--brown); border-bottom: 2px solid var(--brown);
    display: flex; align-items: center; justify-content: center; white-space: nowrap;
  }
  .location-text { font-weight: 700; font-size: 23px; color: var(--ink); }
  .location-text .at { font-weight: 400; font-size: 20px; }
  .intro {
    position: absolute; left: 80px; top: 566px; width: 426px;
    text-align: center; font-size: 23px; line-height: 27.5px; color: var(--ink);
  }
  .facility-photo {
    position: absolute; left: 0; top: 680px; width: 586px; height: 155px;
    background: linear-gradient(#dfe6ea 0%, #c9ccc8 45%, #a6a39a 70%, #7f8d5a 100%);
  }
  .footer-band {
    position: absolute; left: 0; top: 835px; width: 586px; height: 43px; background: var(--brown);
  }
  .tagline-tab {
    position: absolute; left: 27px; top: 817px; width: 153px; height: 61px;
    background: var(--gold); border-radius: 26px 0 0 0;
    clip-path: path("M0 61 L0 26 Q0 0 26 0 L110 0 Q140 0 153 61 Z");
    color: var(--white); font-size: 14.5px; line-height: 14.5px; padding: 12px 0 0 12px;
  }
  .contacts {
    position: absolute; left: 185px; top: 840px; height: 34px;
    display: flex; align-items: center; color: var(--white);
  }
  .phone { padding: 0 8px 0 0; }
  .phone + .phone { border-left: 1px solid #b8926b; padding-left: 8px; }
  .phone-city { display: flex; align-items: center; gap: 2px; font-size: 10.5px; color: var(--gold); line-height: 11px; }
  .phone-number { font-weight: 700; font-size: 14.5px; line-height: 16px; letter-spacing: .3px; }
  .web { border-left: 1px solid #b8926b; padding-left: 8px; font-size: 10.5px; line-height: 13px; }
  .web-line { display: flex; align-items: center; gap: 4px; }
  .dot { width: 8px; height: 6px; background: var(--gold); display: inline-block; }
  .dot.round { width: 7px; height: 7px; border-radius: 50%; }
</style>
</head>
<body>
<main class="ad">
  <svg class="top-rule" viewBox="0 0 586 12" aria-hidden="true">
    <rect x="0" y="0" width="250" height="5" fill="#a8731f"/>
    <polygon points="244,12 252,0 586,0 586,12" fill="#6b3512"/>
  </svg>

  <header class="brand">
    <span class="brand-mark"></span>
    <div class="brand-name">Cobalt Ridge<br>Mini Storage</div>
  </header>

  <div class="garage-art" role="img" aria-label="Illustration of a storage unit with a roll-up door"></div>

  <h1 class="headline">Coming<br>Soon!</h1>

  <div class="location"><span class="location-text">MAPLE AVE <span class="at">@</span> ROUTE 9</span></div>

  <p class="intro">We are a family-owned, premier self-storage facility offering solutions to your Personal Storage, Business Storage and RV &amp; Boat Storage needs.</p>

  <div class="facility-photo" role="img" aria-label="Photo of the storage facility office building with gated storage units"></div>

  <div class="footer-band"></div>
  <div class="tagline-tab">SECURE,<br>CONVENIENT<br>SELF-STORAGE</div>

  <div class="contacts">
    <div class="phone">
      <div class="phone-city"><svg width="8" height="10" viewBox="0 0 8 10"><path d="M4 0a4 4 0 0 1 4 4c0 3-4 6-4 6S0 7 0 4a4 4 0 0 1 4-4z" fill="#a8731f"/><circle cx="4" cy="4" r="1.5" fill="#6b3512"/></svg>Westfield</div>
      <div class="phone-number">210-555-0148</div>
    </div>
    <div class="phone">
      <div class="phone-city"><svg width="8" height="10" viewBox="0 0 8 10"><path d="M4 0a4 4 0 0 1 4 4c0 3-4 6-4 6S0 7 0 4a4 4 0 0 1 4-4z" fill="#a8731f"/><circle cx="4" cy="4" r="1.5" fill="#6b3512"/></svg>Lakeview</div>
      <div class="phone-number">830-555-0192</div>
    </div>
    <div class="web">
      <div class="web-line"><span class="dot"></span>sales@cobaltridgestorage.com</div>
      <div class="web-line"><span class="dot round"></span>www.cobaltridgestorage.com</div>
    </div>
  </div>
</main>
</body>
</html>
```